Plumbing & Heating bussiness card design

i do all plumbing and heating work and need a catchy design. keep it simple but eye catching nothing gimicky
i do 24hr call outs
landlord safety checks
all aspects of plumbing and heating
boiler breakdowns
flue sure reg number 648197
i have put up my old card. not to bothered about the front but i have put up the back for the details. mobile number and office are the same and the email has changed to dantapfixer@brevomail.net

Industry/Entity Type

Safety

Contact Information for Business Card

i do 24hr call outs
landlord safety checks
boiler breakdowns

Requirements
Must have
• i do 24hr call outs
• landlord safety checks
• all aspects of plumbing and heating
• boiler breakdowns
• flue sure reg number 648197

```html
<!DOCTYPE html>
<html lang="en">
<head>
<meta charset="utf-8">
<title>B Harlow Plumbing &amp; Heating – Business Card</title>
<link href="https://fonts.googleapis.com/css2?family=Oswald:wght@400;600;700&family=Open+Sans:wght@400;600;700&display=swap" rel="stylesheet">
<style>
  :root{
    --navy:#1d3f6e;
    --blue:#1f4f8a;
    --red:#d0202e;
    --yellow:#f6b21a;
    --ink:#2a2f3a;
    --paper:#ffffff;
    --stage:#eceef0;
    --chrome-light:#d9dde2;
    --chrome-dark:#5c636b;
  }
  *{box-sizing:border-box;margin:0;padding:0}
  html,body{width:1200px;height:631px;overflow:hidden}
  body{background:var(--stage);font-family:"Open Sans",Arial,sans-serif;color:var(--ink);position:relative}

  .card{position:absolute;top:165px;width:525px;height:300px;background:var(--paper);overflow:hidden;box-shadow:0 6px 18px rgba(0,0,0,.12)}
  .card--front{left:45px}
  .card--back{left:630px}

  /* front */
  .front-photo{position:absolute;left:0;top:0;width:250px;height:300px;
    background:linear-gradient(135deg,var(--chrome-light) 0%,#aeb4bb 40%,var(--chrome-dark) 75%,#8a9199 100%);
    clip-path:polygon(0 0,100% 0,72% 100%,0 100%)}
  .brand{position:absolute;display:flex;align-items:center;gap:8px;font-family:"Oswald",Arial,sans-serif;font-weight:700;color:var(--navy);text-transform:uppercase;line-height:1.05}
  .brand-dot{width:22px;height:22px;border-radius:50%;background:var(--red);flex:none}
  .card--front .brand{left:215px;top:152px;font-size:21px}
  .services{position:absolute;left:300px;top:40px}
  .services h2{font-family:"Oswald",Arial,sans-serif;font-weight:600;font-size:17px;color:var(--navy);letter-spacing:.5px;margin-bottom:6px}
  .services li{list-style:none;font-size:10px;font-weight:600;color:var(--navy);text-transform:uppercase;line-height:1.55}
  .corner-badge{position:absolute;right:0;top:0}

  /* back */
  .back-shade{position:absolute;inset:0;background:linear-gradient(90deg,#eef0f3 0%,#ffffff 55%)}
  .card--back .bands{position:absolute;inset:0}
  .card--back .brand{left:22px;top:70px;font-size:15px}
  .card--back .brand-dot{width:18px;height:18px}
  .person{position:absolute;left:22px;top:125px}
  .person-name{font-family:"Oswald",Arial,sans-serif;font-weight:700;font-size:34px;color:var(--navy);letter-spacing:.5px;line-height:1}
  .person-role{font-family:"Oswald",Arial,sans-serif;font-weight:400;font-size:15px;color:var(--navy);letter-spacing:1px;margin-top:2px}
  .contacts{position:absolute;left:285px;top:72px;list-style:none}
  .contacts li{display:flex;align-items:center;gap:9px;font-size:9px;color:var(--ink);margin-bottom:9px;line-height:1.35}
  .contacts svg{width:12px;height:12px;flex:none;fill:var(--navy)}
  .contacts b{font-weight:700}
</style>
</head>
<body>

<section class="card card--front" aria-label="Card front">
  <div class="front-photo" role="img" aria-label="Photo of a chrome mixer tap over a sink"></div>
  <svg class="corner-badge" width="60" height="60" viewBox="0 0 60 60" aria-hidden="true">
    <polygon points="0,0 60,0 60,60" fill="var(--yellow)"/>
  </svg>
  <div class="services">
    <h2>SERVICES</h2>
    <ul>
      <li>24hr call outs</li>
      <li>Landlord safety checks</li>
      <li>All aspects of plumbing &amp; heating</li>
      <li>Boiler breakdowns</li>
      <li>Flue sure reg no. 648197</li>
    </ul>
  </div>
  <div class="brand"><span class="brand-dot"></span><span>B Harlow<br>Plumbing &amp; Heating</span></div>
</section>

<section class="card card--back" aria-label="Card back">
  <div class="back-shade"></div>
  <svg class="bands" viewBox="0 0 525 300" preserveAspectRatio="none" aria-hidden="true">
    <polygon points="300,0 525,0 525,48 285,48" fill="var(--red)"/>
    <polygon points="0,215 430,215 400,300 0,300" fill="var(--blue)"/>
    <rect x="470" y="232" width="55" height="55" fill="var(--yellow)"/>
  </svg>
  <div class="brand"><span class="brand-dot"></span><span>B Harlow<br>Plumbing &amp; Heating</span></div>
  <div class="person">
    <div class="person-name">TOM REDFERN</div>
    <div class="person-role">FOUNDER</div>
  </div>
  <ul class="contacts">
    <li><svg viewBox="0 0 24 24"><path d="M2 5h20v14H2z M2 5l10 8 10-8" fill="none" stroke="var(--navy)" stroke-width="2"/></svg>dantapfixer@brevomail.net</li>
    <li><svg viewBox="0 0 24 24"><path d="M6 2l4 4-2 3c1 3 4 6 7 7l3-2 4 4-3 4C10 22 2 14 2 5z"/></svg><span><b>Mobile</b> | 07700 900418<br><b>Office</b> | 07700 900418</span></li>
    <li><svg viewBox="0 0 24 24"><path d="M12 3l10 9h-3v9h-5v-6h-4v6H5v-9H2z"/></svg><span>14 Millbrook Road<br>Prestwich, M25 3LT</span></li>
    <li><svg viewBox="0 0 24 24"><circle cx="12" cy="12" r="9" fill="none" stroke="var(--navy)" stroke-width="2"/><path d="M3 12h18M12 3c4 4 4 14 0 18M12 3c-4 4-4 14 0 18" fill="none" stroke="var(--navy)" stroke-width="1.5"/></svg>www.bharlow-ph.example</li>
  </ul>
</section>

</body>
</html>
```